Copperfox Billboard

Please design a billboard using my photos and logos.
For photo of truck please crop the truck itself out and not have the trees / dirt in photo.
Please put " Best Prices in Sevier County"
Please put " 30-yard Dumpsters Starting at 600.00"
Please put " 16-yard Dumpsters Starting at 300.0"
Please put " Delivery and Pickup 7 Days a week"
Billboard size will be 10 ft tall 30 ft wide

```html
<!DOCTYPE html>
<html lang="en">
<head>
<meta charset="utf-8">
<title>Copperfox Dumpsters Billboard</title>
<link href="https://fonts.googleapis.com/css2?family=Bangers&family=Montserrat:wght@700;800&display=swap" rel="stylesheet">
<style>
  :root {
    --sky-top: #b7d1f8;
    --sky-bottom: #ffffff;
    --purple: #8836a2;
    --purple-deep: #660f80;
    --purple-dark: #4e1068;
    --pink: #df8cf5;
    --lilac: #e6a1f7;
    --red: #ee141c;
    --ink: #111111;
    --white: #ffffff;
  }
  html, body {
    margin: 0;
    padding: 0;
    width: 1200px;
    height: 401px;
    overflow: hidden;
    background: var(--white);
  }
  .billboard {
    position: relative;
    width: 1200px;
    height: 401px;
    overflow: hidden;
    font-family: "Montserrat", Arial, sans-serif;
  }
  .billboard__bg {
    position: absolute;
    inset: 0;
  }
  .brand {
    position: absolute;
    left: 150px;
    top: 30px;
    width: 345px;
    color: var(--purple-dark);
    font-weight: 800;
    text-align: right;
    line-height: 1;
    margin: 0;
    white-space: nowrap;
  }
  .brand__name {
    display: block;
    font-size: 58px;
    letter-spacing: 1px;
  }
  .brand__type {
    display: block;
    font-size: 33px;
    letter-spacing: 1px;
    margin-top: 4px;
  }
  .tagline {
    position: absolute;
    left: 77px;
    top: 156px;
    margin: 0;
    font-family: "Bangers", Impact, sans-serif;
    font-size: 44px;
    font-weight: 400;
    letter-spacing: 0.5px;
    color: var(--red);
    -webkit-text-stroke: 1.5px var(--ink);
    text-shadow: 2px 2px 0 var(--ink), -1px -1px 0 var(--white);
    white-space: nowrap;
  }
  .offer {
    position: absolute;
    text-align: center;
    margin: 0;
    line-height: 1;
    white-space: nowrap;
  }
  .offer__size {
    display: block;
    font-size: 29px;
    font-weight: 700;
  }
  .offer__price {
    display: block;
    font-size: 23px;
    font-weight: 800;
    margin-top: 5px;
  }
  .offer--large {
    left: 150px;
    top: 229px;
    width: 372px;
    color: var(--ink);
  }
  .offer--small {
    left: 150px;
    top: 313px;
    width: 372px;
    color: var(--white);
  }
  .service {
    position: absolute;
    left: 750px;
    top: 33px;
    width: 440px;
    text-align: center;
    margin: 0;
    color: var(--white);
    font-weight: 800;
    line-height: 1;
    white-space: nowrap;
    text-shadow: 1.5px 1.5px 0 var(--ink), -1px 1px 0 var(--ink), 1px -1px 0 var(--ink), -1px -1px 0 var(--ink);
  }
  .service__main {
    display: block;
    font-size: 30px;
  }
  .service__days {
    display: block;
    font-size: 23px;
    margin-top: 4px;
  }
  .contact {
    position: absolute;
    left: 600px;
    top: 362px;
    width: 560px;
    height: 26px;
    display: flex;
    align-items: center;
    color: var(--white);
    font-weight: 700;
    font-size: 14px;
  }
  .contact__item {
    display: flex;
    align-items: center;
    gap: 10px;
  }
  .contact__phone { margin-left: 40px; margin-right: auto; }
  .contact__social { margin-left: 40px; }
  .contact__square {
    width: 22px;
    height: 22px;
    border-radius: 5px;
    background: var(--white);
  }
  .contact__circle {
    width: 18px;
    height: 18px;
    border-radius: 50%;
    border: 2.5px solid var(--white);
  }
</style>
</head>
<body>
<main class="billboard">
  <svg class="billboard__bg" width="1200" height="401" viewBox="0 0 1200 401">
    <defs>
      <linearGradient id="sky" x1="0" y1="0" x2="0" y2="1">
        <stop offset="0" stop-color="#b7d1f8"/>
        <stop offset="1" stop-color="#ffffff"/>
      </linearGradient>
      <linearGradient id="truckTone" x1="0" y1="0" x2="1" y2="0">
        <stop offset="0" stop-color="#f2f2f4"/>
        <stop offset="0.55" stop-color="#dcdde2"/>
        <stop offset="0.62" stop-color="#5c2a78"/>
        <stop offset="1" stop-color="#3f1a57"/>
      </linearGradient>
    </defs>

    <rect width="1200" height="401" fill="url(#sky)"/>
    <polygon points="0,0 72,0 0,78" fill="var(--purple)"/>
    <polygon points="72,0 86,0 0,92 0,78" fill="var(--lilac)"/>

    <polygon points="690,0 1200,0 1200,401 540,401 662,219 700,204 790,99" fill="var(--purple)"/>
    <polygon points="660,0 690,0 790,99 700,204 672,204 762,99" fill="var(--lilac)"/>
    <polygon points="775,187 1200,187 1200,204 700,204 716,187" fill="var(--purple-deep)"/>
    <polygon points="574,352 1200,352 1200,401 540,401" fill="var(--purple-deep)"/>

    <polygon points="137,219 662,219 614,291 137,291" fill="var(--pink)"/>
    <polygon points="152,219 137,219 80,291 137,291 137,240" fill="var(--purple-deep)"/>
    <polygon points="137,304 596,304 548,375 137,375" fill="var(--purple-deep)"/>
    <polygon points="137,304 130,304 82,375 137,375" fill="var(--lilac)"/>

    <rect x="540" y="56" width="124" height="170" rx="10" fill="var(--purple)" opacity="0.85"
          role="img" aria-label="Illustration of a purple trash bin launching like a rocket"/>

    <rect x="738" y="110" width="428" height="222" rx="14" fill="url(#truckTone)"
          role="img" aria-label="Photo of a white roll-off truck carrying a purple dumpster"/>

    <path d="M1100,300 L1170,256 M1080,318 L1165,272 M950,338 L1035,296" stroke="var(--purple-dark)" stroke-width="3" stroke-linecap="round"/>

    <circle cx="614" cy="375" r="12" fill="none" stroke="var(--white)" stroke-width="2.5"/>
    <path d="M609,368 q-2,3 2,9 q4,5 8,4 l1,-3 l-3,-2 l-2,2 q-3,-2 -4,-5 l2,-2 l-2,-3 z" fill="var(--white)"/>
  </svg>

  <h1 class="brand">
    <span class="brand__name">COPPERFOX</span>
    <span class="brand__type">DUMPSTERS</span>
  </h1>

  <p class="tagline">BEST PRICES IN SEVIER COUNTY</p>

  <p class="offer offer--large">
    <span class="offer__size">30 YARD DUMPSTER</span>
    <span class="offer__price">STARTING AT 600.00</span>
  </p>

  <p class="offer offer--small">
    <span class="offer__size">16 YARD DUMPSTER</span>
    <span class="offer__price">STARTING AT 300.00</span>
  </p>

  <h2 class="service">
    <span class="service__main">DELIVERY AND PICKUP</span>
    <span class="service__days">7 DAYS A WEEK</span>
  </h2>

  <div class="contact">
    <span class="contact__item contact__phone">XX-XX-XXXX</span>
    <span class="contact__item contact__social"><span class="contact__square"></span>Linkly</span>
    <span class="contact__item contact__social"><span class="contact__circle"></span>Pixgram</span>
  </div>
</main>
</body>
</html>
```